Music Industry Business Needs a Business Card Design

Copper Lantern is an audio mastering company that has been in business for 20 years. Mastering is the final creative step in the music production chain. Our job is to make the music sound as good as it possibly can prior to release to the public. Our world is technical, artistic, precise. We work on everything from independent artists to the music for the Grandfield Cup. We are looking for a new, more modern business card design. I am uploading a copy of our logo, although it doesn't absolutely need to be included in the design.

Target Market(s)

Music Industry Professionals

Industry/Entity Type

Business

Contact Information for Business Card

Address, Phone, Email, Website, Name, Job Title

Font styles to use
Sans Serif

Requirements
Must have
• Sorry, but I don't have any concrete things to request. If I had a clear idea of what I want, I would probably just design something myself. I am looking for fresh input and thought I would try this.
Should not have
• Anything that is typical, such as headphones or the like.

```html
<!DOCTYPE html>
<html lang="en">
<head>
<meta charset="utf-8">
<title>Copper Lantern — Business Card</title>
<link href="https://fonts.googleapis.com/css2?family=Montserrat:wght@300;400&family=Oswald:wght@500&display=swap" rel="stylesheet">
<style>
  :root {
    --backdrop: #1c1d1f;
    --card-light: #8e9092;
    --card-mid: #7a7c7f;
    --card-dark: #4a4b4e;
    --curve-edge: #3b3c3f;
    --wordmark: #2e2f31;
    --contact: #c9cacc;
    --name: #d6d7d9;
    --accent: #3aa4dc;
  }
  html, body {
    margin: 0;
    width: 1200px;
    height: 804px;
    overflow: hidden;
    background: var(--backdrop);
  }
  .stage {
    width: 1200px;
    height: 804px;
    display: flex;
    align-items: center;
    justify-content: center;
  }
  .card {
    position: relative;
    width: 1050px;
    height: 600px;
    border-radius: 26px;
    overflow: hidden;
    background: linear-gradient(135deg, var(--card-light), var(--card-mid));
    font-family: "Montserrat", sans-serif;
  }
  .card__curve {
    position: absolute;
    inset: 0;
    width: 100%;
    height: 100%;
  }
  .wordmark {
    position: absolute;
    margin: 0;
    font-family: "Montserrat", sans-serif;
    font-weight: 400;
    color: var(--wordmark);
    line-height: 1;
    letter-spacing: -2px;
    text-shadow: 2px 3px 4px rgba(0,0,0,0.25);
  }
  .wordmark--top { left: 130px; top: 130px; font-size: 122px; }
  .wordmark--bottom { right: 60px; bottom: 88px; font-size: 112px; }
  .person {
    position: absolute;
    right: 70px;
    top: 178px;
    text-align: right;
  }
  .person__name {
    font-family: "Oswald", sans-serif;
    font-weight: 500;
    font-size: 34px;
    color: var(--name);
    letter-spacing: 1px;
    line-height: 1;
  }
  .person__title {
    font-family: "Oswald", sans-serif;
    font-weight: 500;
    font-size: 18px;
    color: var(--accent);
    letter-spacing: 3.5px;
    line-height: 1.3;
  }
  .contact {
    position: absolute;
    left: 80px;
    top: 318px;
    font-size: 16px;
    font-weight: 300;
    color: var(--contact);
    line-height: 30px;
  }
  .contact__row { display: flex; gap: 70px; }
  .contact__item { display: flex; align-items: center; gap: 8px; white-space: nowrap; }
  .contact__icon { width: 13px; height: 13px; fill: var(--accent); flex: none; }
  .website {
    position: absolute;
    left: 130px;
    top: 468px;
    font-family: "Oswald", sans-serif;
    font-weight: 500;
    font-size: 17px;
    letter-spacing: 6px;
    color: var(--contact);
  }
</style>
</head>
<body>
<main class="stage">
  <article class="card">
    <svg class="card__curve" viewBox="0 0 1050 600" preserveAspectRatio="none" aria-hidden="true">
      <path d="M0,210 C120,120 300,60 520,50 C640,45 660,190 670,330 C680,470 700,560 760,600 L0,600 Z" fill="var(--card-dark)"/>
      <path d="M0,210 C120,120 300,60 520,50 C640,45 660,190 670,330 C680,470 700,560 760,600" fill="none" stroke="var(--curve-edge)" stroke-width="3"/>
      <path d="M670,330 C700,480 760,560 880,560 C980,560 1050,520 1050,520 L1050,600 L760,600 C700,560 680,470 670,330 Z" fill="#ffffff" opacity="0.06"/>
    </svg>

    <h1 class="wordmark wordmark--top">COPPER</h1>
    <p class="wordmark wordmark--bottom">LANTERN</p>

    <div class="person">
      <div class="person__name">MARA LINDQVIST</div>
      <div class="person__title">MASTERING ENGINEER</div>
    </div>

    <address class="contact" style="font-style:normal">
      <div class="contact__row">
        <span class="contact__item">
          <svg class="contact__icon" viewBox="0 0 24 24"><path d="M6.6 10.8a15.1 15.1 0 0 0 6.6 6.6l2.2-2.2c.3-.3.7-.4 1-.2 1.1.4 2.3.6 3.6.6.6 0 1 .4 1 1V20c0 .6-.4 1-1 1A17 17 0 0 1 3 4c0-.6.4-1 1-1h3.5c.6 0 1 .4 1 1 0 1.3.2 2.5.6 3.6.1.3 0 .7-.2 1z"/></svg>
          (555) 014-2290
        </span>
        <span class="contact__item">
          <svg class="contact__icon" viewBox="0 0 24 24"><path d="M2 5h20v14H2z M2 5l10 8 10-8" /></svg>
          hello@copperlantern.ca
        </span>
      </div>
      <div class="contact__row">
        <span class="contact__item">
          <svg class="contact__icon" viewBox="0 0 24 24"><path d="M12 2a7 7 0 0 0-7 7c0 5.2 7 13 7 13s7-7.8 7-13a7 7 0 0 0-7-7zm0 9.5A2.5 2.5 0 1 1 12 6.5a2.5 2.5 0 0 1 0 5z"/></svg>
          118 - 7 Avenue S.W. Ridgefield, Ontario, Canada K0A 1B2
        </span>
      </div>
    </address>

    <div class="website">WWW.COPPERLANTERN.CA</div>
  </article>
</main>
</body>
</html>
```